We need a DL size flyer, double sided, for our lawn mowing and gardening business, Kestrel Yards.

We want to run on the front side, the following promotion:
50% off lawn mowing, applies to first lawn mowed on any regular service,
applies to first 100 callers only, so call now!
Professional lawn mowing at an affordable price.

Logo at the bottom left, with Lawn and Garden Maintenance written just below logo.

On bottom Right contact details;
Tom and Gareth
Ph: 0487650912
Email: kestrelyards@mailbox-demo.com
www.kestrelyards-demo.com.au

Front side positioned horizontally, with a bright and colour full design in the background, with the offer of 50% Off lawn mowing in large letters along the top.

On the rear side, also positioned horizontally, a list of our services, stating;

At Kestrel Yards we specialise in the following services;
Lawn mowing
Edging
Blowing
Hedging
Pruning
Tree Loping
Weeding
Poisoning
Mulching
Fertilising
Rubbish removal
Planting
Lawn care and advice
Turf
And any other garden maintenance job,
No job too big or too small.
(No particular order, whatever fits best)
Also include our contact details,
Kestrel Yards
Ph 0487650912
www.kestrelyards-demo.com.au

Target Market(s)

Home owners, aged between 30-50 years old, moderate socio ecenomic status to more afluent areas.

Industry/Entity Type

Business

Requirements
Must have
• DL size, front and back, full colour.
Nice to have
• The writting stating "Kestrel Yards" in our logo is quite bland, if that could also be amended to make it more appealing, but change the writting design only not the actual logo.

```html
<!DOCTYPE html>
<html lang="en">
<head>
<meta charset="utf-8">
<title>Kestrel Yards – DL Flyer</title>
<link rel="stylesheet" href="https://fonts.googleapis.com/css2?family=Anton&family=Questrial&display=swap">
<style>
  :root {
    --backdrop: #7a5f47;
    --card-white: #ffffff;
    --grass-light: #c9e08a;
    --grass: #9cc648;
    --grass-deep: #7fae2e;
    --ink: #1c1c1c;
    --panel: rgba(255, 255, 255, 0.55);
  }
  * { box-sizing: border-box; margin: 0; padding: 0; }
  html, body { width: 1200px; height: 761px; overflow: hidden; }
  body {
    background: var(--backdrop);
    position: relative;
    font-family: "Questrial", "Century Gothic", sans-serif;
    color: var(--ink);
  }
  .flyer {
    position: absolute;
    width: 740px;
    height: 350px;
    overflow: hidden;
    box-shadow: 0 4px 14px rgba(0, 0, 0, 0.35);
  }

  /* ---------- Front ---------- */
  .flyer--front {
    left: 40px; top: 40px;
    background: linear-gradient(180deg, var(--card-white) 0%, var(--card-white) 22%, var(--grass-light) 50%, var(--grass) 70%, var(--grass-deep) 100%);
  }
  .front__grass {
    position: absolute; left: 0; right: 0; top: 90px; height: 120px;
    background: linear-gradient(180deg, rgba(255,255,255,0) 0%, rgba(156,198,72,0.45) 60%, rgba(156,198,72,0) 100%);
  }
  .offer {
    position: absolute; left: 28px; top: 78px;
    font-family: "Anton", "Impact", sans-serif;
    line-height: 1;
    display: flex; align-items: flex-start;
  }
  .offer__figure { font-size: 150px; letter-spacing: -3px; }
  .offer__suffix { display: flex; flex-direction: column; margin-left: 4px; margin-top: 12px; }
  .offer__percent { font-size: 64px; }
  .offer__off { font-size: 56px; margin-top: -2px; }
  .headline {
    position: absolute; left: 250px; top: 6px;
    font-family: "Anton", "Impact", sans-serif;
    font-size: 82px; line-height: 1; letter-spacing: -0.5px;
  }
  .promo {
    position: absolute; left: 318px; top: 108px; width: 392px;
    padding: 8px 12px 10px;
    background: var(--panel);
    border-radius: 14px;
    text-align: center;
  }
  .promo__call { font-size: 27px; margin-bottom: 4px; }
  .promo__line { font-size: 14.5px; line-height: 1.3; }
  .contact {
    position: absolute; left: 318px; top: 238px; width: 392px;
    text-align: center; font-size: 15.5px; line-height: 1.3;
  }
  .contact__names { font-size: 18px; margin-bottom: 2px; }
  .brand {
    position: absolute; left: 30px; top: 268px;
    display: flex; align-items: center; gap: 8px;
  }
  .brand__dot { width: 22px; height: 22px; border-radius: 50%; background: var(--ink); }
  .brand__name { font-size: 22px; color: var(--ink); }
  .brand__tagline {
    position: absolute; left: 30px; top: 306px;
    font-size: 13.5px;
  }

  /* ---------- Back ---------- */
  .flyer--back {
    left: 420px; top: 372px;
    background: linear-gradient(180deg, var(--card-white) 0%, var(--card-white) 55%, #eaf3d4 78%, var(--grass-light) 100%);
  }
  .back__grass {
    position: absolute; right: 0; bottom: 0; width: 460px; height: 230px;
    background: linear-gradient(200deg, rgba(201,224,138,0) 20%, rgba(156,198,72,0.35) 70%, rgba(127,174,46,0.5) 100%);
  }
  .services__intro {
    position: absolute; left: 28px; top: 24px;
    font-size: 22px;
  }
  .services__list {
    position: absolute; list-style: disc; font-size: 15px; line-height: 1.55;
    padding-left: 18px;
  }
  .services__list--one { left: 48px; top: 78px; }
  .services__list--two { left: 268px; top: 78px; }
  .services__list--three { left: 488px; top: 78px; width: 200px; }
  .back__footer {
    position: absolute; left: 0; right: 0; top: 250px;
    text-align: center; font-size: 15px; line-height: 1.3;
  }
  .back__slogan { font-size: 19px; margin-bottom: 2px; }
</style>
</head>
<body>

  <section class="flyer flyer--front" aria-label="Flyer front">
    <div class="front__grass" role="img" aria-label="Grass blades rising across the card"></div>
    <h1 class="headline">Lawn Mowing</h1>
    <div class="offer">
      <span class="offer__figure">50</span>
      <span class="offer__suffix">
        <span class="offer__percent">%</span>
        <span class="offer__off">Off</span>
      </span>
    </div>
    <div class="promo">
      <p class="promo__call">Call now!</p>
      <p class="promo__line">For the first lawn mowed on any regular service.</p>
      <p class="promo__line">Applies to first 100 callers only.</p>
      <p class="promo__line">Professional lawn mowing at an affordable price.</p>
    </div>
    <div class="contact">
      <p class="contact__names">Tom and Gareth</p>
      <p>0487650912</p>
      <p>kestrelyards@mailbox-demo.com</p>
      <p>www.kestrelyards-demo.com.au</p>
    </div>
    <div class="brand">
      <span class="brand__dot"></span>
      <span class="brand__name">Kestrel Yards</span>
    </div>
    <p class="brand__tagline">Lawn &amp; Gardening Maintenance</p>
  </section>

  <section class="flyer flyer--back" aria-label="Flyer back">
    <div class="back__grass" role="img" aria-label="Grass blades along the lower right"></div>
    <h2 class="services__intro">At Kestrel Yards we specialise in the following services:</h2>
    <ul class="services__list services__list--one">
      <li>Lawn mowing</li>
      <li>Edging</li>
      <li>Blowing</li>
      <li>Hedging</li>
      <li>Pruning</li>
      <li>Tree Loping</li>
    </ul>
    <ul class="services__list services__list--two">
      <li>Weeding</li>
      <li>Poisoning</li>
      <li>Mulching</li>
      <li>Fertilising</li>
      <li>Rubbish removal</li>
      <li>Planting</li>
    </ul>
    <ul class="services__list services__list--three">
      <li>Lawn care and advice</li>
      <li>Turf</li>
      <li>All any other garden maintenance job</li>
    </ul>
    <div class="back__footer">
      <p class="back__slogan">NO JOB TOO BIG OR TOO SMALL.</p>
      <p>Kestrel Yards</p>
      <p>Ph 0487650912</p>
      <p>www.kestrelyards-demo.com.au</p>
    </div>
  </section>

</body>
</html>
```